Website Design for Landscaping/Concrete Company

I need a website that is informative about what my company does and also offers before and after pictures of completed work. I already have a logo. The website must say "FREE ESTIMATES" somewhere and list a phone number. I would like to stick with the logo colors or similar (black and lime green).
Services Offered by Dornel Contractors:
Landscaping
Mowing
Concrete
Sidewalks
Brush Removal
Land Beautification

Please list the company name in large letters DORNEL CONTRACTORS
and also the contact information in large font.

Right now I am looking for a somewhat coverpage for my website. I don't have a lot of information for people to point and click on yet. Id like to get a coverpage to get my name out and then have a designer come back in a few months and update with more pictures and information.
Updates

If allowed please submit projects after due date. I made a mistake and only posted for one day. Thanks.

Coding

Coded - Design and coding required

```html
<!DOCTYPE html>
<html lang="en">
<head>
<meta charset="utf-8">
<title>Dornel Contractors</title>
<link href="https://fonts.googleapis.com/css2?family=Oswald:wght@400;500;600;700&family=Open+Sans:wght@400;600;700&display=swap" rel="stylesheet">
<style>
:root{
  --lime:#8cb314;
  --lime-dark:#769a0c;
  --ink:#222;
  --charcoal:#2b2b2b;
  --text:#666;
  --light:#f2f2f2;
  --white:#fff;
}
*{box-sizing:border-box;margin:0;padding:0}
html,body{width:1200px;height:4960px;overflow:hidden}
body{font-family:"Open Sans",sans-serif;color:var(--text);background:var(--white);font-size:14px;line-height:1.7;position:relative}
h1,h2,h3,h4,.btn,.nav a{font-family:"Oswald",sans-serif}
.wrap{width:960px;margin:0 auto;position:relative}
.btn{display:inline-block;background:var(--lime);color:var(--white);font-size:13px;font-weight:500;text-transform:uppercase;padding:12px 26px;letter-spacing:.5px;line-height:1.4}
.eyebrow{color:var(--lime);font-size:11px;text-transform:uppercase;letter-spacing:1.5px;font-weight:600}
.section-title{font-size:32px;color:var(--ink);font-weight:600;line-height:1.2}
.center{text-align:center}
.brand{display:flex;align-items:center;gap:10px;font-family:"Oswald",sans-serif;font-weight:600;font-size:18px;color:var(--lime);text-transform:uppercase;line-height:1.1}
.brand .mark{width:26px;height:26px;background:var(--lime);flex:none}

/* hero */
.hero{position:relative;height:912px;background:linear-gradient(180deg,#4a5d3a 0%,#6f8a55 45%,#8a9a7a 70%,#b8bdb2 100%)}
.topbar{height:40px;background:rgba(20,20,20,.75);color:#ddd;font-size:12px}
.topbar .wrap{display:flex;justify-content:space-between;align-items:center;height:40px}
.topbar-contact span{margin-right:24px}
.topbar .social{display:flex;gap:8px}
.topbar .social i{display:block;width:22px;height:22px;background:var(--lime);border-radius:50%}
.header .wrap{display:flex;align-items:center;justify-content:space-between;height:100px}
.nav{display:flex;gap:36px}
.nav a{color:var(--white);text-decoration:none;font-size:14px;text-transform:uppercase;font-weight:500}
.hero-content{position:absolute;top:340px;left:0;right:0;text-align:center;color:var(--white)}
.hero-content .eyebrow{color:var(--white);font-size:13px}
.hero-content h1{font-size:78px;font-weight:700;letter-spacing:2px;line-height:1.1;margin:6px 0 14px}
.hero-content p{width:560px;margin:0 auto 34px;color:#eee;font-size:14px}

.features{position:absolute;top:752px;left:120px;width:960px;display:flex;gap:28px;z-index:2}
.feature{flex:1;background:var(--lime);color:var(--white);text-align:center;padding:44px 30px;height:280px}
.feature.dark{background:var(--charcoal)}
.feature .num{font-family:"Oswald",sans-serif;font-size:40px;line-height:1;border:2px solid rgba(255,255,255,.6);display:inline-block;padding:6px 14px}
.feature h3{font-size:20px;margin:14px 0 10px;font-weight:500;line-height:1.3}
.feature p{font-size:12px;color:#f1f1f1}

/* about */
.about{height:640px;padding-top:188px}
.about .wrap{display:flex;gap:50px;align-items:flex-start}
.about-photo{position:relative;width:410px;height:380px;background:linear-gradient(160deg,#e6e6e6,#b9c7a0);flex:none}
.about-photo .tab{position:absolute;left:-30px;top:40px;width:58px;height:200px;background:var(--lime);color:var(--white);font-family:"Oswald",sans-serif;font-size:12px;writing-mode:vertical-rl;transform:rotate(180deg);display:flex;align-items:center;justify-content:center;letter-spacing:1px}
.about-text{flex:1;padding-top:10px}
.about-text h2{font-size:28px;color:var(--ink);margin-bottom:16px;line-height:1.2}
.about-text ul{list-style:none;margin:16px 0}
.about-text li{display:flex;align-items:center;gap:10px;font-size:13px;margin-bottom:6px}
.about-text li svg{flex:none}

/* banner */
.garden{height:208px;background:linear-gradient(90deg,#2a2a25 0%,#3a3d30 60%,#4d5a3a 100%)}
.garden .wrap{display:flex;justify-content:space-between;align-items:center;height:208px}
.garden h2{font-size:32px;color:var(--white);font-weight:500}
.garden p{color:#ccc;font-size:13px}

/* services */
.services{height:900px;padding-top:60px}
.services .intro{width:560px;margin:10px auto 40px;font-size:13px}
.service-grid{display:grid;grid-template-columns:repeat(3,280px);gap:20px 60px;justify-content:center}
.service .img{height:190px}
.service .cap{background:#ececec;height:100px;position:relative;display:flex;align-items:flex-end;justify-content:center;padding-bottom:22px}
.service .cap h4{font-size:18px;color:var(--ink);font-weight:500}
.service .icon{position:absolute;top:-34px;left:50%;margin-left:-34px;width:68px;height:68px;border-radius:50%;background:var(--lime);border:4px solid #ececec;display:flex;align-items:center;justify-content:center}

/* estimates */
.estimates{height:400px;background:linear-gradient(90deg,var(--lime-dark) 0%,var(--lime) 55%,#a4b86a 70%,#667a45 100%);color:var(--white);position:relative}
.estimates .wrap{padding-top:60px}
.estimates .col{width:540px}
.estimates h2{font-size:36px;font-weight:600;margin-bottom:12px;line-height:1.2}
.estimates p{font-size:13px;color:#f3f3f3}
.estimates .call{display:flex;align-items:center;gap:14px;margin:22px 0}
.estimates .call .ic{width:48px;height:48px;border-radius:50%;border:2px solid var(--white);display:flex;align-items:center;justify-content:center}
.estimates .call small{display:block;font-size:11px;text-transform:uppercase;letter-spacing:1px}
.estimates .call strong{font-family:"Oswald",sans-serif;font-size:26px;font-weight:500;line-height:1.2}
.estimates .photo{position:absolute;right:0;top:0;width:480px;height:400px;background:linear-gradient(120deg,rgba(140,179,20,0),#4f6a2c 40%,#2f4020)}

/* work */
.work{height:560px;padding-top:50px}
.gallery{display:flex;gap:20px;margin-top:40px;height:300px}
.gallery .shot{flex:1;position:relative}
.gallery .shot .tag{position:absolute;bottom:10px;color:var(--white);font-family:"Oswald",sans-serif;font-size:12px}
.gallery .center-shot{display:flex}
.gallery .center-shot .half{flex:1;position:relative}
.gallery .divider{position:absolute;left:50%;top:0;bottom:0;width:3px;background:var(--white);margin-left:-1px}
.gallery .knob{position:absolute;left:50%;top:50%;width:40px;height:40px;margin:-20px;border-radius:50%;background:var(--white);display:flex;align-items:center;justify-content:center}
.dots{display:flex;gap:8px;justify-content:center;margin-top:26px}
.dots i{width:10px;height:10px;border-radius:50%;background:#ccc}
.dots i.on{background:var(--lime)}

/* testimonials */
.testimonials{height:460px;background:var(--light);padding-top:90px}
.testimonials .wrap{display:flex;gap:40px}
.testimonials .lead{width:300px}
.testimonials .lead p{font-size:13px;margin-top:14px}
.quote{width:260px;text-align:center}
.quote .box{background:var(--lime);color:var(--white);padding:28px 22px;font-size:13px;position:relative;height:200px}
.quote .box::after{content:"";position:absolute;bottom:-12px;left:50%;margin-left:-12px;border:12px solid transparent;border-bottom:0;border-top-color:var(--lime)}
.quote h4{font-size:15px;color:var(--ink);margin-top:28px;font-weight:500}

/* contact */
.contact{height:500px;padding-top:50px;position:relative;background:linear-gradient(90deg,#fff 70%,#e6ebdc 85%,#b2c08e 100%)}
.contact .form-area{width:560px;margin:0 auto;text-align:center;position:relative}
.contact h2{font-size:34px;color:var(--ink);font-weight:600;line-height:1.3}
.contact .sub{font-size:13px;margin:6px 0 30px}
.fields{display:grid;grid-template-columns:1fr 1fr;gap:16px}
.field{border:1px solid #ddd;background:var(--white);height:46px;text-align:left;padding:12px 14px;font-size:12px;color:#999}
.field.area{grid-column:1/3;height:130px}
.contact .btn{margin-top:26px}
.contact .side{position:absolute;right:0;top:30px;width:240px;height:440px;background:linear-gradient(200deg,#6f8a45,#c9d3b4 70%,rgba(255,255,255,0))}

/* footer */
.footer{height:332px;background:var(--charcoal);color:#bbb;padding-top:60px}
.footer .wrap{display:flex;justify-content:space-between}
.footer .col1{width:260px}
.footer .col1 p{font-size:12px;margin:18px 0}
.footer .social{display:flex;gap:8px}
.footer .social i{width:28px;height:28px;border-radius:50%;background:var(--lime);display:block}
.footer h4{color:var(--white);font-size:22px;font-weight:500;margin-bottom:14px}
.footer ul{list-style:none;font-size:13px}
.footer ul li{margin-bottom:6px}
.footer .info li{display:flex;gap:10px;align-items:center}
.copy{height:48px;background:var(--lime);color:var(--white);font-size:12px;text-align:center;line-height:48px}
</style>
</head>
<body>

<section class="hero" role="img" aria-label="Photo of a worker trimming grass along a garden path">
  <div class="topbar">
    <div class="wrap">
      <div class="topbar-contact"><span>+1 555 014 2290</span><span>info@dornelbuild.com</span></div>
      <div class="social"><i></i><i></i><i></i></div>
    </div>
  </div>
  <header class="header">
    <div class="wrap">
      <div class="brand"><span class="mark"></span>Dornel<br>Contractors</div>
      <nav class="nav"><a>Home</a><a>About</a><a>Services</a><a>Our Work</a><a>Contact</a></nav>
      <span class="btn">Free Quote</span>
    </div>
  </header>
  <div class="hero-content">
    <div class="eyebrow">Your partner in landscaping</div>
    <h1>DORNEL CONTRACTORS</h1>
    <p>Lawn, garden and concrete work done right the first time. We plan, build and care for outdoor spaces that look great in every season.</p>
    <span class="btn">Our Services</span>
  </div>
</section>

<div class="features">
  <div class="feature">
    <span class="num">01</span>
    <h3>Modern Equipment</h3>
    <p>We use new, well kept machines that handle every job quickly and leave your yard neat and clean.</p>
  </div>
  <div class="feature dark">
    <span class="num">02</span>
    <h3>Professional Services</h3>
    <p>Our trained crew brings years of hands-on skill to each project, big or small, from start to finish.</p>
  </div>
  <div class="feature">
    <span class="num">03</span>
    <h3>Free Estimates</h3>
    <p>Call us today for a free, no obligation estimate and a clear plan for your outdoor project.</p>
  </div>
</div>

<section class="about">
  <div class="wrap">
    <div class="about-photo" role="img" aria-label="Portrait of a gardener in green uniform holding hedge shears">
      <div class="tab">15 YEARS OF EXPERIENCE</div>
    </div>
    <div class="about-text">
      <div class="eyebrow">Company's introduction</div>
      <h2>Dornel Contractors</h2>
      <p>We are a local team that cares for lawns, gardens and concrete. We listen to your ideas and turn them into tidy, lasting outdoor spaces you can enjoy.</p>
      <ul>
        <li><svg width="16" height="16" viewBox="0 0 16 16"><circle cx="8" cy="8" r="8" fill="#8cb314"/><path d="M4.5 8.2l2.3 2.3 4.7-4.8" stroke="#fff" stroke-width="1.8" fill="none"/></svg>Free estimates and hours that suit you</li>
        <li><svg width="16" height="16" viewBox="0 0 16 16"><circle cx="8" cy="8" r="8" fill="#8cb314"/><path d="M4.5 8.2l2.3 2.3 4.7-4.8" stroke="#fff" stroke-width="1.8" fill="none"/></svg>Using modern equipment while working</li>
        <li><svg width="16" height="16" viewBox="0 0 16 16"><circle cx="8" cy="8" r="8" fill="#8cb314"/><path d="M4.5 8.2l2.3 2.3 4.7-4.8" stroke="#fff" stroke-width="1.8" fill="none"/></svg>High qualified crew on every job</li>
        <li><svg width="16" height="16" viewBox="0 0 16 16"><circle cx="8" cy="8" r="8" fill="#8cb314"/><path d="M4.5 8.2l2.3 2.3 4.7-4.8" stroke="#fff" stroke-width="1.8" fill="none"/></svg>Providing high quality work in our area</li>
      </ul>
      <p>From weekly mowing to new sidewalks, we take pride in every detail and keep our promises on time and on budget.</p>
    </div>
  </div>
</section>

<section class="garden" role="img" aria-label="Dark photo of a garden being worked on">
  <div class="wrap">
    <div>
      <h2>Are you looking to upgrade your garden?</h2>
      <p>Talk with our team about fresh plantings, clean edges and new paths for your home.</p>
    </div>
    <span class="btn">Contact Us</span>
  </div>
</section>

<section class="services center">
  <div class="eyebrow">What we're offering</div>
  <h2 class="section-title">Our Services</h2>
  <p class="intro">We offer a full range of outdoor services for homes and businesses. Every project gets the same careful work and friendly service.</p>
  <div class="service-grid">
    <div class="service"><div class="img" role="img" aria-label="Photo of a landscaped garden" style="background:linear-gradient(160deg,#6c8a3a,#3f5a25)"></div><div class="cap"><div class="icon"><svg width="28" height="28" viewBox="0 0 28 28"><path d="M14 4c6 4 6 12 0 16-6-4-6-12 0-16zM14 20v5" stroke="#fff" stroke-width="2" fill="none"/></svg></div><h4>Landscaping</h4></div></div>
    <div class="service"><div class="img" role="img" aria-label="Photo of a lawn being mowed" style="background:linear-gradient(160deg,#8aa45a,#4e6a2a)"></div><div class="cap"><div class="icon"><svg width="28" height="28" viewBox="0 0 28 28"><rect x="6" y="12" width="16" height="7" fill="none" stroke="#fff" stroke-width="2"/><circle cx="9" cy="21" r="2.5" fill="#fff"/><circle cx="19" cy="21" r="2.5" fill="#fff"/><path d="M18 12l4-7" stroke="#fff" stroke-width="2"/></svg></div><h4>Mowing</h4></div></div>
    <div class="service"><div class="img" role="img" aria-label="Photo of a stone and concrete garden bed" style="background:linear-gradient(160deg,#5a6470,#3a4a3a)"></div><div class="cap"><div class="icon"><svg width="28" height="28" viewBox="0 0 28 28"><rect x="5" y="7" width="8" height="6" fill="#fff"/><rect x="15" y="7" width="8" height="6" fill="#fff"/><rect x="5" y="15" width="18" height="6" fill="#fff"/></svg></div><h4>Concrete</h4></div></div>
    <div class="service"><div class="img" role="img" aria-label="Photo of a paved sidewalk with plants" style="background:linear-gradient(160deg,#9a9a7a,#5a6a3a)"></div><div class="cap"><div class="icon"><svg width="28" height="28" viewBox="0 0 28 28"><path d="M10 4L6 24M18 4l4 20M14 6v3M14 13v3M14 20v3" stroke="#fff" stroke-width="2"/></svg></div><h4>Sidewalks</h4></div></div>
    <div class="service"><div class="img" role="img" aria-label="Photo of a worker clearing brush" style="background:linear-gradient(160deg,#5f7a35,#2f4520)"></div><div class="cap"><div class="icon"><svg width="28" height="28" viewBox="0 0 28 28"><path d="M6 22L20 8M16 6l6 6M8 10l10 10" stroke="#fff" stroke-width="2"/></svg></div><h4>Brush Removal</h4></div></div>
    <div class="service"><div class="img" role="img" aria-label="Photo of a trimmed garden with shrubs" style="background:linear-gradient(160deg,#7a9a45,#3d5a22)"></div><div class="cap"><div class="icon"><svg width="28" height="28" viewBox="0 0 28 28"><circle cx="14" cy="11" r="6" fill="none" stroke="#fff" stroke-width="2"/><path d="M14 17v8M9 25h10" stroke="#fff" stroke-width="2"/></svg></div><h4>Land Beautification</h4></div></div>
  </div>
</section>

<section class="estimates">
  <div class="photo" role="img" aria-label="Photo of a gardener trimming a hedge"></div>
  <div class="wrap">
    <div class="col">
      <h2>Free Estimates!</h2>
      <p>Tell us about your yard and we will visit, measure and give you a clear price at no cost. No pressure, just honest advice on what your space needs.</p>
      <div class="call">
        <div class="ic"><svg width="22" height="22" viewBox="0 0 24 24"><path d="M6.6 10.8a15 15 0 006.6 6.6l2.2-2.2c.3-.3.7-.4 1-.2 1.1.4 2.3.6 3.6.6.6 0 1 .4 1 1V20c0 .6-.4 1-1 1A17 17 0 013 4c0-.6.4-1 1-1h3.5c.6 0 1 .4 1 1 0 1.3.2 2.5.6 3.6.1.3 0 .7-.2 1z" fill="#fff"/></svg></div>
        <div><small>Call us anytime</small><strong>+1 555 014 2290</strong></div>
      </div>
      <p>Or send us a short note and we will call you back within one business day to book your visit.</p>
    </div>
  </div>
</section>

<section class="work">
  <div class="wrap center">
    <div class="eyebrow">Our completed work</div>
    <h2 class="section-title">Recent Work</h2>
  </div>
  <div class="gallery">
    <div class="shot" role="img" aria-label="Photo of a finished lawn" style="background:linear-gradient(160deg,#4a5a3a,#2e3a26)"></div>
    <div class="shot center-shot">
      <div class="half" role="img" aria-label="Before photo of an overgrown yard" style="background:linear-gradient(160deg,#6a6a55,#3f4a30)"><span class="tag" style="left:12px">BEFORE</span></div>
      <div class="half" role="img" aria-label="After photo of a clean landscaped yard" style="background:linear-gradient(160deg,#8a9a6a,#4f6a35)"><span class="tag" style="right:12px">AFTER</span></div>
      <div class="divider"></div>
      <div class="knob"><svg width="20" height="12" viewBox="0 0 20 12"><path d="M6 1L1 6l5 5M14 1l5 5-5 5" stroke="#8cb314" stroke-width="2" fill="none"/></svg></div>
    </div>
    <div class="shot" role="img" aria-label="Photo of a new concrete path" style="background:linear-gradient(160deg,#5a5f55,#333a2e)"></div>
  </div>
  <div class="dots"><i></i><i class="on"></i><i></i></div>
</section>

<section class="testimonials">
  <div class="wrap">
    <div class="lead">
      <div class="eyebrow">What our customers say</div>
      <h2 class="section-title">Our Testimonials</h2>
      <p>Our neighbors trust us with their homes. Here is what a few of them say about our work and our crew.</p>
    </div>
    <div class="quote">
      <div class="box">"Dornel Contractors rebuilt our front walk and cleaned up the whole yard. The crew was on time, polite and the result looks amazing. Highly recommended!"</div>
      <h4>Rena Colby</h4>
    </div>
    <div class="quote">
      <div class="box">"They mow our lawn every week and it has never looked better. Fair prices, friendly team and they always leave everything spotless."</div>
      <h4>Elias Brandt</h4>
    </div>
  </div>
</section>

<section class="contact">
  <div class="side" role="img" aria-label="Photo of hands cutting a branch with pruning shears"></div>
  <div class="form-area">
    <h2>Get In Touch With Us!</h2>
    <p class="sub">Drop us a line and we will be in touch soon to plan your project.</p>
    <div class="fields">
      <div class="field">Full Name</div>
      <div class="field">Email Address</div>
      <div class="field">Phone Number</div>
      <div class="field">Subject</div>
      <div class="field area">Message here</div>
    </div>
    <span class="btn">Send Message</span>
  </div>
</section>

<footer class="footer">
  <div class="wrap">
    <div class="col1">
      <div class="brand"><span class="mark"></span>Dornel<br>Contractors</div>
      <p>Local landscaping and concrete crew serving homes and businesses with care and pride for over fifteen years.</p>
      <div class="social"><i></i><i></i><i></i></div>
    </div>
    <div>
      <h4>Quick Links</h4>
      <ul><li>Home</li><li>About</li><li>Services</li><li>Work</li><li>Contact</li></ul>
    </div>
    <div>
      <h4>Information</h4>
      <ul class="info">
        <li><svg width="14" height="16" viewBox="0 0 14 18"><path d="M7 0a7 7 0 00-7 7c0 5 7 11 7 11s7-6 7-11a7 7 0 00-7-7zm0 9.5A2.5 2.5 0 117 4.5a2.5 2.5 0 010 5z" fill="#8cb314"/></svg>18 Marlow Lane, Fenwick, USA</li>
        <li><svg width="14" height="12" viewBox="0 0 16 12"><rect width="16" height="12" fill="#8cb314"/><path d="M0 0l8 6 8-6" stroke="#2b2b2b" fill="none"/></svg>info@dornelbuild.com</li>
        <li><svg width="14" height="14" viewBox="0 0 24 24"><path d="M6.6 10.8a15 15 0 006.6 6.6l2.2-2.2c.3-.3.7-.4 1-.2 1.1.4 2.3.6 3.6.6.6 0 1 .4 1 1V20c0 .6-.4 1-1 1A17 17 0 013 4c0-.6.4-1 1-1h3.5c.6 0 1 .4 1 1 0 1.3.2 2.5.6 3.6.1.3 0 .7-.2 1z" fill="#8cb314"/></svg>+1 555 014 2290</li>
      </ul>
    </div>
  </div>
</footer>
<div class="copy">Copyright © 2024 DORNEL CONTRACTORS. All Rights Reserved.</div>

</body>
</html>
```